JAR LABEL FOR GUMMIES

I need a design of a label for jar with Gummy candies:
- label size: 21.5 cm length, 5.4 cm height with rounded angles. The size of the label is in attached.
-The label must include the name of the product BRIMO VITAMIN D, as the second word (VITAMIN D) may be situated under the name BRIMO or slighly down on the right.
-The shape of the gummies is hearts, so the label must include an illustration of 1 or 2 hearts.
-From the text in attached the information in green should be in the center, that is visible at the front of the label.
-The logo of the Company - QLW is also in attached and there is no need to be in front. The rest of the information of the label must be situated on the right and left side of the center part.

-A white, empty space with dimesnions around 5 cm long and 1 sm height should be left on the back, so the recycle icons will be inserted later on.
-The destination of the products is kids and adults.
-The jar is transparent with aluminium cap - gold or silver color.
We are looking for a playful of stylish design of the label. The product will be sold mostly in pharmacies, where there is huge competition, so it has to capture the attention. We would like to highlight the NO COLOURS, NATURAL FLAVOURS writing and 36 PECTING GUMMY CANDIES as well. The product will have different variations so it will be appreciated if the design is provided in few colors – if possible strong colors.

In attched I am providing:
- bar code
- logo of the company - QLW
- the dimensions of the label
- the text for the label.
- photo of the jar for the label

Target Market(s)

Kids and adults

Industry/Entity Type

NUTRACEUTICAL

Colors
00AB8E
00BBA5
67D7C9
C6EFE9
E9F9F6
FFC000
F8CF3A
FAE287
FDF2CF
FEFAEE
F0912C
F2A743
F7CA91
FBE8D2
FDF5EE
EB3D1F
EC4F4E
F09395
F8D3D4
FCEDEE
E54698
E96AAD
F1A4CE
F9D9EA
FCEFF6
A7469A
B969AE
D3A5CF
EDDBEB
F8F0F9

Requirements
Must have
• HEART DESIGN, NICE ACTIVE COLOURS

```html
<!DOCTYPE html>
<html lang="en">
<head>
<meta charset="utf-8">
<title>BRIMO Vitamin D – Gummy Jar Labels</title>
<link rel="stylesheet" href="https://fonts.googleapis.com/css2?family=Lilita+One&family=Barlow+Condensed:wght@500;600&family=Mulish:wght@500&display=swap">
<style>
  :root {
    --stage: #aed8d7;
    --label-bg: #f4f4f4;
    --ink: #151515;
    --gold: #c9a24b;
    --gold-soft: #dcc28a;
    --red: #d2202c;
    --red-soft: #e2606a;
    --blue: #1d4590;
    --blue-soft: #5a7db5;
    --pink: #c2185f;
    --pink-soft: #d9619e;
  }
  * { box-sizing: border-box; margin: 0; padding: 0; }
  html, body { width: 1200px; height: 960px; overflow: hidden; }
  body { background: var(--stage); position: relative; }

  .label {
    position: absolute;
    width: 341px; height: 222px;
    background: var(--label-bg);
    border-radius: 6px;
    overflow: hidden;
  }
  .label--gold { left: 242px; top: 180px; --accent: var(--gold); --accent-soft: var(--gold-soft); }
  .label--red  { left: 617px; top: 180px; --accent: var(--red);  --accent-soft: var(--red-soft); }
  .label--blue { left: 242px; top: 610px; --accent: var(--blue); --accent-soft: var(--blue-soft); }
  .label--pink { left: 617px; top: 610px; --accent: var(--pink); --accent-soft: var(--pink-soft); }

  .side-band {
    position: absolute; left: 0; top: 0;
    width: 70px; height: 205px;
    background: var(--accent);
    border-bottom-right-radius: 60px;
  }
  .heart-art {
    position: absolute; left: 10px; top: 55px;
    width: 160px; height: 150px;
    border-radius: 50% 50% 46% 46%;
    background: linear-gradient(120deg, var(--accent-soft), var(--accent));
    border: 2px solid var(--label-bg);
  }
  .badges { position: absolute; left: 32px; top: 8px; display: flex; flex-direction: column; gap: 8px; }
  .badge {
    display: flex; align-items: center; gap: 3px;
    height: 16px; padding-right: 6px;
    background: var(--accent); color: #fff;
    font: 500 8.5px/1 "Mulish", sans-serif; letter-spacing: .2px;
    border-radius: 8px;
  }
  .badge__icon {
    width: 18px; height: 18px; margin-left: -2px;
    border-radius: 50%; background: var(--accent);
    border: 1.5px solid #fff; box-shadow: 0 0 0 1px var(--accent);
  }

  .brand {
    position: absolute; right: 16px; top: 6px;
    font: 400 46px/1 "Lilita One", sans-serif; color: var(--ink);
    letter-spacing: 1px;
  }
  .product {
    position: absolute; right: 16px; top: 55px;
    font: 400 30px/1 "Lilita One", sans-serif; color: var(--ink);
    letter-spacing: 1px;
  }
  .category {
    position: absolute; right: 17px; top: 95px;
    padding: 2px 8px;
    background: var(--accent); color: #fff;
    font: 600 17px/1.05 "Barlow Condensed", sans-serif; letter-spacing: .6px;
    border-radius: 4px;
  }
  .claim {
    position: absolute; right: 23px; top: 125px;
    text-align: right;
    font: 500 11px/1.3 "Mulish", sans-serif; color: var(--ink);
  }
  .facts { position: absolute; right: 17px; top: 163px; display: flex; gap: 5px; }
  .fact {
    width: 32px; height: 42px;
    border: 1.5px solid var(--accent);
    border-radius: 5px 5px 10px 10px;
    background: #fff; overflow: hidden;
    display: flex; flex-direction: column;
    text-align: center; font-family: "Barlow Condensed", sans-serif;
  }
  .fact__value { height: 20px; display: flex; align-items: center; justify-content: center; color: var(--ink); font-weight: 600; font-size: 13px; line-height: .9; }
  .fact__value--big { font-size: 18px; }
  .fact__value--small { font-size: 5.5px; }
  .fact__key { flex: 1; background: var(--accent); color: #fff; font-size: 5px; font-weight: 500; line-height: 1.05; display: flex; align-items: center; justify-content: center; }
  .base-rule { position: absolute; left: 0; right: 0; top: 214px; height: 1.5px; background: var(--ink); }
</style>
</head>
<body>

<section class="label label--gold">
  <div class="side-band"></div>
  <div class="heart-art" role="img" aria-label="Illustration of two outlined hearts in gold tones"></div>
  <div class="badges"><span class="badge"><i class="badge__icon"></i>LACTOSE FREE</span><span class="badge"><i class="badge__icon"></i>GLUTEN FREE</span></div>
  <h1 class="brand">BRIMO</h1>
  <h2 class="product">VITAMIN D</h2>
  <p class="category">FOOD SUPPLEMENT</p>
  <p class="claim">WITH NATURAL FLAVOURS<br>AND NO COLOURS</p>
  <div class="facts">
    <div class="fact"><span class="fact__value">144 G</span><span class="fact__key">NET<br>WEIGHT</span></div>
    <div class="fact"><span class="fact__value fact__value--big">36</span><span class="fact__key">PECTIN<br>GUMMY<br>CANDIES</span></div>
    <div class="fact"><span class="fact__value fact__value--small">VANILLA<br>LEMON</span><span class="fact__key">FLAVOUR</span></div>
  </div>
  <div class="base-rule"></div>
</section>

<section class="label label--red">
  <div class="side-band"></div>
  <div class="heart-art" role="img" aria-label="Illustration of two outlined hearts in red tones"></div>
  <div class="badges"><span class="badge"><i class="badge__icon"></i>LACTOSE FREE</span><span class="badge"><i class="badge__icon"></i>GLUTEN FREE</span></div>
  <h1 class="brand">BRIMO</h1>
  <h2 class="product">VITAMIN D</h2>
  <p class="category">FOOD SUPPLEMENT</p>
  <p class="claim">WITH NATURAL FLAVOURS<br>AND NO COLOURS</p>
  <div class="facts">
    <div class="fact"><span class="fact__value">144 G</span><span class="fact__key">NET<br>WEIGHT</span></div>
    <div class="fact"><span class="fact__value fact__value--big">36</span><span class="fact__key">PECTIN<br>GUMMY<br>CANDIES</span></div>
    <div class="fact"><span class="fact__value fact__value--small">FLAVOR<br>VARIANT</span><span class="fact__key">FLAVOUR</span></div>
  </div>
  <div class="base-rule"></div>
</section>

<section class="label label--blue">
  <div class="side-band"></div>
  <div class="heart-art" role="img" aria-label="Illustration of two outlined hearts in blue tones"></div>
  <div class="badges"><span class="badge"><i class="badge__icon"></i>LACTOSE FREE</span><span class="badge"><i class="badge__icon"></i>GLUTEN FREE</span></div>
  <h1 class="brand">BRIMO</h1>
  <h2 class="product">VITAMIN D</h2>
  <p class="category">FOOD SUPPLEMENT</p>
  <p class="claim">WITH NATURAL FLAVOURS<br>AND NO COLOURS</p>
  <div class="facts">
    <div class="fact"><span class="fact__value">144 G</span><span class="fact__key">NET<br>WEIGHT</span></div>
    <div class="fact"><span class="fact__value fact__value--big">36</span><span class="fact__key">PECTIN<br>GUMMY<br>CANDIES</span></div>
    <div class="fact"><span class="fact__value fact__value--small">FLAVOR<br>VARIANT</span><span class="fact__key">FLAVOUR</span></div>
  </div>
  <div class="base-rule"></div>
</section>

<section class="label label--pink">
  <div class="side-band"></div>
  <div class="heart-art" role="img" aria-label="Illustration of two outlined hearts in pink tones"></div>
  <div class="badges"><span class="badge"><i class="badge__icon"></i>LACTOSE FREE</span><span class="badge"><i class="badge__icon"></i>GLUTEN FREE</span></div>
  <h1 class="brand">BRIMO</h1>
  <h2 class="product">VITAMIN D</h2>
  <p class="category">FOOD SUPPLEMENT</p>
  <p class="claim">WITH NATURAL FLAVOURS<br>AND NO COLOURS</p>
  <div class="facts">
    <div class="fact"><span class="fact__value">144 G</span><span class="fact__key">NET<br>WEIGHT</span></div>
    <div class="fact"><span class="fact__value fact__value--big">36</span><span class="fact__key">PECTIN<br>GUMMY<br>CANDIES</span></div>
    <div class="fact"><span class="fact__value fact__value--small">FLAVOR<br>VARIANT</span><span class="fact__key">FLAVOUR</span></div>
  </div>
  <div class="base-rule"></div>
</section>

</body>
</html>
```